Portal Panel Medic need professional looking business card printed on plastic, Commericial, Industri

We are family owned and operated garage door company in Indianapolis, Indiana. We sale service and install dock equipment, doors, operators. We are looking to expand our commercial/ industrial division. We also service all residential doors and operators. We are looking for a business that stands out of the crowd. We are committed to have the best customer service in the industry.

Target Market(s)

National and local general contractors, National/ Corpate service accounts,

Industry/Entity Type

Business Service

Contact Information for Business Card

To be printed on plastic stock

Font styles to use
Sans Serif

Colors
ffffff
f04a50
ec1f27

Requirements
Must have
• Name, website,email, phone number, position.
Nice to have
• A standout professional design

```html
<!DOCTYPE html>
<html lang="en">
<head>
<meta charset="utf-8">
<title>Portal Panel Medic — Business Card</title>
<link rel="stylesheet" href="https://fonts.googleapis.com/css2?family=Questrial&display=swap">
<style>
  :root {
    --white: #ffffff;
    --red-soft: #f04a50;
    --red: #ec1f27;
    --ink: #0b0b0b;
    --stage: #333333;
    --text: #2a2a2a;
  }
  * { margin: 0; padding: 0; box-sizing: border-box; }
  html, body { width: 1200px; height: 1200px; overflow: hidden; }
  body {
    background: var(--stage);
    font-family: "Questrial", "Century Gothic", sans-serif;
    position: relative;
  }
  .card {
    position: absolute;
    left: 120px;
    width: 960px;
    height: 540px;
    overflow: hidden;
  }
  .card--front {
    top: 40px;
    background: radial-gradient(circle at 50% 50%, #f05a60 0%, var(--red-soft) 25%, var(--red) 70%);
  }
  .card--back {
    top: 620px;
    background: var(--white);
  }
  .brand {
    position: absolute;
    text-transform: uppercase;
    line-height: 0.95;
    letter-spacing: 1px;
    text-align: center;
  }
  .card--front .brand {
    left: 50%; top: 50%;
    transform: translate(-50%, -50%);
    color: var(--white);
    font-size: 62px;
  }
  .card--back .brand {
    left: 234px; top: 286px;
    transform: translate(-50%, -50%);
    color: var(--red);
    font-size: 40px;
  }
  .contact-rail {
    position: absolute;
    left: 457px; top: 53px;
    width: 110px; height: 461px;
    background: var(--ink);
    border-radius: 55px;
    display: flex;
    flex-direction: column;
  }
  .contact-rail__slot {
    flex: 1;
    display: flex;
    align-items: center;
    justify-content: center;
    border-bottom: 1px solid #2c2c2c;
  }
  .contact-rail__slot:last-child { border-bottom: none; }
  .contact-rail__slot svg { width: 26px; height: 26px; fill: var(--white); }
  .details {
    position: absolute;
    left: 607px; top: 0;
    width: 260px; height: 100%;
    color: var(--text);
  }
  .details__name, .details__role {
    position: absolute; left: 0;
    font-size: 27px;
    letter-spacing: 0.5px;
  }
  .details__name { top: 60px; }
  .details__role { top: 92px; font-size: 24px; }
  .details__rule {
    position: absolute; left: 0;
    width: 247px; height: 2px;
    background: var(--red-soft);
  }
  .details__item {
    position: absolute; left: 0;
    font-size: 16px;
    line-height: 1.2;
  }
</style>
</head>
<body>
  <section class="card card--front" aria-label="Card front">
    <div class="brand">Portal<br>Panel<br>Medic</div>
  </section>

  <section class="card card--back" aria-label="Card back">
    <div class="brand">Portal<br>Panel<br>Medic</div>

    <div class="contact-rail">
      <div class="contact-rail__slot">
        <svg viewBox="0 0 24 24" aria-hidden="true"><circle cx="12" cy="7" r="5"/><path d="M2 22c0-6 4.5-9 10-9s10 3 10 9z"/></svg>
      </div>
      <div class="contact-rail__slot">
        <svg viewBox="0 0 24 24" aria-hidden="true"><path d="M6.6 10.8a15 15 0 0 0 6.6 6.6l2.2-2.2a1 1 0 0 1 1-.25 11.4 11.4 0 0 0 3.6.57 1 1 0 0 1 1 1V20a1 1 0 0 1-1 1A17 17 0 0 1 3 4a1 1 0 0 1 1-1h3.5a1 1 0 0 1 1 1c0 1.25.2 2.45.57 3.57a1 1 0 0 1-.25 1z"/></svg>
      </div>
      <div class="contact-rail__slot">
        <svg viewBox="0 0 24 24" aria-hidden="true"><path d="M2 5h20v14H2z M3.5 6.5 12 13l8.5-6.5" fill="none" stroke="#fff" stroke-width="0"/><path d="M2 5h20v2l-10 7L2 7z"/><path d="M2 9l10 7 10-7v10H2z"/></svg>
      </div>
      <div class="contact-rail__slot">
        <svg viewBox="0 0 24 24" aria-hidden="true" style="fill:none;stroke:#fff;stroke-width:1.6"><circle cx="12" cy="12" r="9"/><ellipse cx="12" cy="12" rx="4" ry="9"/><path d="M3 12h18M4.5 7.5h15M4.5 16.5h15"/></svg>
      </div>
      <div class="contact-rail__slot">
        <svg viewBox="0 0 24 24" aria-hidden="true"><path d="M12 2a7 7 0 0 0-7 7c0 5.2 7 13 7 13s7-7.8 7-13a7 7 0 0 0-7-7zm0 9.5A2.5 2.5 0 1 1 12 6.5a2.5 2.5 0 0 1 0 5z"/></svg>
      </div>
    </div>

    <div class="details">
      <p class="details__name">MARA</p>
      <p class="details__role">COO DIRECTOR</p>
      <span class="details__rule" style="top:146px"></span>
      <p class="details__item" style="top:178px">(317)555-0148</p>
      <span class="details__rule" style="top:229px"></span>
      <p class="details__item" style="top:262px">www.PortalPanelMedic.com</p>
      <span class="details__rule" style="top:317px"></span>
      <p class="details__item" style="top:346px">www.PortalPanelMedic.com</p>
      <span class="details__rule" style="top:407px"></span>
      <p class="details__item" style="top:437px">12th Larkspur Avenue<br>Northvale, USA 404040</p>
    </div>
  </section>
</body>
</html>
```